Meadowlark Learning Growth Partners (MLGP)

This is a professional business card. Logo and picture are a must on the front of the card. I am an educational consultant. I have been consulting for the past three years for a company. I am now opening my own company. My goal for my consulting company is to eventually consult all over America.

Target Market(s)

Educators, schools, professionals

Industry/Entity Type

Consulting

Contact Information for Business Card

Picture/logo on front, simple modern design

Font styles to use
Serif

Colors
85abd2
0355a3
3176b5
cedeed

Requirements
Must have
• picture, logo,
• Odessa Pruitt, Ed.S
• address 5073 Cormorant ridge Dr. Nashville, TN 37940
• Cell:616-555-0148
• Office: 629-555-0172
• www.Mlgpedu.example
• pruittodessa@mailbox.example

```html
<!DOCTYPE html>
<html lang="en">
<head>
<meta charset="utf-8">
<title>Meadowlark Learning Growth Partners – Business Card</title>
<link rel="stylesheet" href="https://fonts.googleapis.com/css2?family=Roboto:wght@400;500;700&family=Roboto+Condensed:wght@700&display=swap">
<style>
  :root {
    --backdrop: #2b2b2d;
    --card: #1d1d1f;
    --card-edge: #252527;
    --brand-blue: #0355a3;
    --mid-blue: #3176b5;
    --soft-blue: #85abd2;
    --pale-blue: #cedeed;
    --text-light: #f2f2f2;
    --portrait-dark: #1e2330;
    --portrait-light: #c9c2b8;
  }
  * { box-sizing: border-box; margin: 0; padding: 0; }
  html, body { width: 1200px; height: 900px; overflow: hidden; }
  body {
    background: var(--backdrop);
    font-family: "Roboto", Arial, sans-serif;
    position: relative;
  }
  .card {
    position: absolute;
    width: 665px;
    height: 380px;
    background: linear-gradient(160deg, var(--card-edge), var(--card));
    box-shadow: 0 10px 30px rgba(0,0,0,0.45);
    overflow: hidden;
  }
  /* Front */
  .card-front { left: 420px; top: 60px; }
  .brand {
    position: absolute;
    left: 58px;
    top: 128px;
    display: flex;
    align-items: center;
  }
  .brand-mark {
    width: 46px; height: 46px;
    border-radius: 50%;
    background: var(--brand-blue);
    margin-right: 14px;
  }
  .brand-initials {
    font-weight: 700;
    font-size: 30px;
    letter-spacing: 2px;
    color: var(--brand-blue);
  }
  .brand-divider {
    width: 1px; height: 54px;
    background: var(--brand-blue);
    margin: 0 12px 0 14px;
  }
  .brand-name {
    font-weight: 700;
    font-size: 12.5px;
    line-height: 14px;
    color: var(--brand-blue);
    width: 120px;
  }
  .front-web {
    position: absolute;
    left: 60px;
    top: 210px;
    font-size: 15px;
    letter-spacing: 7px;
    color: var(--text-light);
  }
  .portrait {
    position: absolute;
    right: 0; top: 70px;
    width: 270px; height: 310px;
    background: radial-gradient(ellipse at 50% 30%, var(--portrait-light) 0 28%, transparent 29%),
                linear-gradient(180deg, #2a2a2c 0%, var(--portrait-dark) 60%, #15171d 100%);
  }
  /* Back */
  .card-back { left: 115px; top: 475px; }
  .holder-name {
    position: absolute;
    left: 50px;
    top: 150px;
    font-family: "Roboto Condensed", "Arial Narrow", sans-serif;
    font-weight: 700;
    font-size: 26px;
    color: var(--brand-blue);
    text-transform: uppercase;
  }
  .back-divider {
    position: absolute;
    left: 352px; top: 95px;
    width: 2px; height: 150px;
    background: linear-gradient(180deg, transparent, #d8d8d8 50%, transparent);
  }
  .contact {
    position: absolute;
    left: 380px; top: 105px;
    color: var(--text-light);
    font-size: 17px;
    line-height: 21px;
  }
  .address { margin-bottom: 14px; }
  .contact-list { list-style: none; }
  .contact-list li { display: flex; align-items: center; height: 23px; }
  .contact-list svg { width: 15px; height: 15px; margin-right: 10px; fill: var(--brand-blue); }
</style>
</head>
<body>
  <section class="card card-front">
    <div class="brand">
      <span class="brand-mark"></span>
      <span class="brand-initials">MLGP</span>
      <span class="brand-divider"></span>
      <span class="brand-name">Meadowlark Learning Growth Partners</span>
    </div>
    <p class="front-web">www.Mlgpedu.example</p>
    <div class="portrait" role="img" aria-label="Portrait photograph of Odessa Pruitt in a dark blazer and white blouse"></div>
  </section>

  <section class="card card-back">
    <h1 class="holder-name">Odessa Pruitt, Ed.S</h1>
    <span class="back-divider"></span>
    <div class="contact">
      <p class="address">5073 Cormorant ridge Dr.<br>Nashville, TN 37940</p>
      <ul class="contact-list">
        <li><svg viewBox="0 0 24 24"><path d="M6.6 10.8a15.1 15.1 0 0 0 6.6 6.6l2.2-2.2c.3-.3.7-.4 1-.2 1.1.4 2.3.6 3.6.6.6 0 1 .4 1 1V20c0 .6-.4 1-1 1A17 17 0 0 1 3 4c0-.6.4-1 1-1h3.5c.6 0 1 .4 1 1 0 1.3.2 2.5.6 3.6.1.3 0 .7-.2 1z"/></svg>629-555-0172</li>
        <li><svg viewBox="0 0 24 24"><path d="M7 1h10c1.1 0 2 .9 2 2v18c0 1.1-.9 2-2 2H7c-1.1 0-2-.9-2-2V3c0-1.1.9-2 2-2zm0 3v14h10V4zm5 15.5a1 1 0 1 0 0 2 1 1 0 0 0 0-2z"/></svg>616-555-0148</li>
        <li><svg viewBox="0 0 24 24"><path d="M2 5h20v14H2zm2 2v.5l8 5 8-5V7zm0 2.8V17h16V9.8l-8 5z"/></svg>pruittodessa@mailbox.example</li>
        <li><svg viewBox="0 0 24 24"><path d="M12 2a10 10 0 1 0 0 20 10 10 0 0 0 0-20zm0 2c1.2 1.4 2 3.5 2.3 7H9.7C10 7.5 10.8 5.4 12 4zm-3.4 7H4.1a8 8 0 0 1 5-6.3A13 13 0 0 0 8.6 11zm0 2c.1 2.4.6 4.6 1.5 6.3A8 8 0 0 1 4.1 13zm1.1 0h4.6c-.3 3.5-1.1 5.6-2.3 7-1.2-1.4-2-3.5-2.3-7zm5.7 0h4.5a8 8 0 0 1-5 6.3c.9-1.7 1.4-3.9 1.5-6.3zm0-2a13 13 0 0 0-1.5-6.3 8 8 0 0 1 5 6.3z"/></svg>www.Mlgpedu.example</li>
      </ul>
    </div>
  </section>
</body>
</html>
```